Pool Screen Enclosure Building a Career Boot Camp!

Looking to Host a Boot Camp for people looking for a career or looking to change careers. We Design, Manufacture and Install Custom Pool Screen Enclosures. We have a training program to allow Non Experienced motivated people the chance at a great career that will provide a great living for them and their family. This will be a paid boot camp, week long, we provide all the initial training for them to make a transition into our business. This will be 5 days of training with a guaranteed job to start the following Monday.... This is good for both someone with no construction experience or someone with construction experience that wants to upgrade their current job.
Paid Boot Camp
transition to a full time job with great pay
Benefits include Health Insurance, Dental and Vision, 401K, we provide the tools and training.

```html
<!DOCTYPE html>
<html lang="en">
<head>
<meta charset="utf-8">
<title>Paid Boot Camp – Lanai Works</title>
<link href="https://fonts.googleapis.com/css2?family=Montserrat:wght@400;500;600;700;800&display=swap" rel="stylesheet">
<style>
:root{
  --green:#6cbf44;
  --yellow:#f5b71b;
  --black:#0a0a0a;
  --ink:#1b1b1b;
  --paper:#ffffff;
  --paper-shade:#e9e9e9;
}
*{margin:0;padding:0;box-sizing:border-box}
html,body{width:950px;height:1200px;overflow:hidden;background:var(--paper)}
body{font-family:"Montserrat",sans-serif;color:var(--ink)}
.flyer{position:relative;width:950px;height:1200px;overflow:hidden;
  background:linear-gradient(180deg,var(--paper-shade) 0%,#f7f7f7 18%,#ffffff 45%,#f4f4f4 80%,#e6e6e6 100%)}
.header-band{position:absolute;left:0;top:0;width:950px;height:164px;background:var(--black)}
.brand{position:absolute;left:52px;top:62px;display:flex;align-items:center;gap:14px}
.brand-dot{width:44px;height:44px;border-radius:50%;background:var(--green)}
.brand-name{font-weight:700;font-size:34px;color:var(--green);letter-spacing:-.5px}
.hero-band{position:absolute;left:0;top:175px;width:950px;height:326px;background:var(--green)}
.hero-title{position:absolute;left:46px;top:206px;color:#fff;text-shadow:2px 3px 4px rgba(0,0,0,.35)}
.hero-title .paid{display:block;font-weight:800;font-size:136px;line-height:1;letter-spacing:-2px}
.hero-title .camp{display:block;font-weight:800;font-size:55px;line-height:1;margin-top:-4px;letter-spacing:.5px}
.hero-sub{position:absolute;left:52px;top:410px;font-weight:700;font-size:27px;line-height:33px;color:var(--black)}
.art{position:absolute;left:0;top:0}
.copy{position:absolute;left:42px;font-size:17.5px;line-height:27px;color:var(--ink);font-weight:500}
.copy em{font-style:normal;color:var(--green);font-weight:600}
.copy.intro{top:566px;width:500px}
.copy.program{top:697px;width:840px}
.copy.camp{top:790px;width:525px}
.copy.fit{top:936px;width:500px}
.benefits{position:absolute;left:594px;top:770px;width:331px;height:312px;border:2px dashed var(--green);border-radius:12px;padding:12px 16px 0}
.benefits h2{font-weight:800;font-size:26px;line-height:32px;color:var(--green);text-decoration:underline;text-underline-offset:4px;letter-spacing:.2px;white-space:nowrap}
.benefits h2 span{color:var(--yellow)}
.benefits ul{list-style:none;margin-top:15px}
.benefits li{display:flex;gap:8px;align-items:flex-start;font-weight:700;font-size:20px;line-height:24px;padding:6px 0 6px 10px;border-bottom:2px solid var(--black);margin-bottom:21px}
.benefits li:last-child{margin-bottom:0}
.tick{flex:none;width:19px;height:19px;margin-top:3px}
.footer{position:absolute;left:0;top:1111px;width:950px;height:55px}
.footer-addr{position:absolute;left:82px;top:1116px;font-weight:700;font-size:17px;line-height:22px;color:var(--black)}
.footer-contact{position:absolute;left:428px;top:1120px;display:flex;align-items:center;gap:14px;color:var(--black)}
.footer-contact .phone{font-weight:800;font-size:25px}
.footer-contact .bar{width:3px;height:28px;background:var(--black)}
.footer-contact .mail{font-weight:600;font-size:17px}
</style>
</head>
<body>
<main class="flyer">
  <div class="header-band"></div>
  <div class="hero-band"></div>

  <svg class="art" width="950" height="680" viewBox="0 0 950 680">
    <defs>
      <linearGradient id="photoTone" x1="0" y1="0" x2="0" y2="1">
        <stop offset="0" stop-color="#9aa4ac"/>
        <stop offset=".35" stop-color="#5d6468"/>
        <stop offset=".6" stop-color="#7c8a84"/>
        <stop offset="1" stop-color="#5f8f92"/>
      </linearGradient>
      <linearGradient id="thumbTone" x1="0" y1="0" x2="0" y2="1">
        <stop offset="0" stop-color="#a9b3b8"/>
        <stop offset="1" stop-color="#6f7a72"/>
      </linearGradient>
    </defs>
    <path d="M565 0 C500 90 468 200 474 320 C478 420 520 480 560 500 L950 600 L950 0 Z" fill="#ffffff"/>
    <path role="img" aria-label="Photo of a finished screened pool enclosure at dusk" d="M578 0 C512 92 482 200 488 318 C492 412 530 470 570 490 L950 585 L950 0 Z" fill="url(#photoTone)"/>
    <circle cx="515" cy="373" r="85" fill="#fff"/>
    <circle role="img" aria-label="Photo of trainees reviewing enclosure plans" cx="515" cy="373" r="79" fill="url(#thumbTone)"/>
    <circle cx="635" cy="530" r="85" fill="#fff"/>
    <circle role="img" aria-label="Photo of workers installing an enclosure roof" cx="635" cy="530" r="79" fill="url(#thumbTone)"/>
    <circle cx="836" cy="575" r="85" fill="#fff"/>
    <circle role="img" aria-label="Photo of an enclosure frame being assembled" cx="836" cy="575" r="79" fill="url(#thumbTone)"/>
  </svg>

  <div class="brand"><span class="brand-dot"></span><span class="brand-name">Lanai Works</span></div>

  <h1 class="hero-title"><span class="paid">PAID</span><span class="camp">BOOT CAMP</span></h1>
  <p class="hero-sub">TRANSITION TO A FULL<br>TIME JOB WITH GREAT PAY</p>

  <p class="copy intro">Looking to Host a Boot Camp for people looking for a career or looking to change careers. We <em>Design, Manufacture</em> and <em>Install Custom Pool Screen Enclosures</em>.</p>
  <p class="copy program">We have a <em>training program</em> to allow <em>Non Experienced motivated people</em> the chance at a great career that will provide a great living for them and their family.</p>
  <p class="copy camp">This will be a <em>PAID BOOT CAMP</em>, week long, we provide all the initial training for them to make a transition into our business. This will be <em>5 DAYS</em> of training with a <em>GUARANTEED JOB</em> to start the following Monday....</p>
  <p class="copy fit">This is good for both someone with no <em>CONSTRUCTION EXPERIENCE</em> or someone with construction experience that wants to upgrade their current job.</p>

  <section class="benefits">
    <h2>BENEFITS <span>INCLUDE:</span></h2>
    <ul>
      <li><svg class="tick" viewBox="0 0 20 20"><circle cx="10" cy="10" r="8.5" fill="none" stroke="#6cbf44" stroke-width="2"/><path d="M5.5 10.5l3 3 6-7" fill="none" stroke="#6cbf44" stroke-width="2.4" stroke-linecap="round"/></svg>Health Insurance</li>
      <li><svg class="tick" viewBox="0 0 20 20"><circle cx="10" cy="10" r="8.5" fill="none" stroke="#6cbf44" stroke-width="2"/><path d="M5.5 10.5l3 3 6-7" fill="none" stroke="#6cbf44" stroke-width="2.4" stroke-linecap="round"/></svg>Dental and Vision</li>
      <li><svg class="tick" viewBox="0 0 20 20"><circle cx="10" cy="10" r="8.5" fill="none" stroke="#6cbf44" stroke-width="2"/><path d="M5.5 10.5l3 3 6-7" fill="none" stroke="#6cbf44" stroke-width="2.4" stroke-linecap="round"/></svg>401K</li>
      <li><svg class="tick" viewBox="0 0 20 20"><circle cx="10" cy="10" r="8.5" fill="none" stroke="#6cbf44" stroke-width="2"/><path d="M5.5 10.5l3 3 6-7" fill="none" stroke="#6cbf44" stroke-width="2.4" stroke-linecap="round"/></svg>We provide the tools<br>and training</li>
    </ul>
  </section>

  <svg class="footer" viewBox="0 0 950 55" aria-hidden="true">
    <polygon points="0,0 382,0 356,55 0,55" fill="#6cbf44"/>
    <polygon points="392,0 950,0 950,55 366,55" fill="#f5b71b"/>
  </svg>
  <p class="footer-addr">418 HARBOR PALM AVE,<br>CORAL BEND FL 34000</p>
  <p class="footer-contact"><span class="phone">555-214-0398</span><span class="bar"></span><span class="mail">admin@lanaiworks.com</span></p>
</main>
</body>
</html>
```